April 11th Event- Islamorada- Coaching/Tarot/Hypnotherapy

Hi! Need a flyer that can also be posted on social media. Directions attached. Also will need a version that 2 can fit on 1 piece of paper so I can cut in half for hand outs. PDF example attached as well so you can understand. Thank you!

AAAAAAAAAAAAAAAAAAAAAAAAAAAAAAAAAAAAAAAAAAAAAAAAAAAAAAAAAAAAAAAAAAAAAAAAAAAAAAAAAAAAAAAAAAAAAAAAAAAAAAAAAAAAAAAAAAAAAAAAAAAAAAAAAAAAAAAAAAAAAAAAAAAAAAAAAAAAAAAAAAAAAAAAAAAAAAAAAAAAAAAAAAAAAAAAAAAAAAAAAAAAAAAAAAAAAAAAAAAAAAAAAA

Target Market(s)

Female audience age 35-70.
Spiritual, sophisticated

Industry/Entity Type

Event Planning

Font styles to use
Serif

Colors
d2a4cc
3176b5
85acd3
b868aa
e667a6
eea4c8
f59296
fbf289
add136

Requirements
Must have
• See attachments
Nice to have
• See attachments

```html
<!DOCTYPE html>
<html lang="en">
<head>
<meta charset="utf-8">
<title>Get the 411 – An Evening of Self Discovery</title>
<link rel="stylesheet" href="https://fonts.googleapis.com/css2?family=Bebas+Neue&family=Bungee+Inline&family=Open+Sans:wght@400;700&family=Yellowtail&display=swap">
<style>
  :root {
    --pink: #f2c6cc;
    --rose: #d9767c;
    --gold: #d1a544;
    --gold-dark: #b98a2c;
    --gold-light: #f0d77a;
    --teal: #4a7f88;
    --ink: #2d2d2d;
    --grey: #666;
    --red: #d8141a;
    --white: #ffffff;
  }
  * { margin: 0; padding: 0; box-sizing: border-box; }
  html, body { width: 889px; height: 1200px; overflow: hidden; background: var(--white); }
  .flyer { position: relative; width: 889px; height: 1200px; overflow: hidden; background: var(--white); font-family: "Open Sans", sans-serif; color: var(--ink); }
  .abs { position: absolute; }

  .hero-wash { left: 0; top: 0; }
  .mandala-top { right: 0; top: 0; width: 250px; height: 360px; background: radial-gradient(circle at 70% 30%, rgba(225,160,170,.35), rgba(255,255,255,0) 70%); }
  .mandala-bottom { left: 0; bottom: 60px; width: 300px; height: 300px; background: radial-gradient(circle at 20% 80%, rgba(0,0,0,.05), rgba(255,255,255,0) 70%); }
  .hero-frame { left: 0; top: 0; }

  .headline { left: 185px; width: 523px; text-align: center; font-family: "Bebas Neue", sans-serif; line-height: 1; }
  .headline-411 { top: 52px; font-size: 128px; color: var(--white); transform: scaleX(.8); letter-spacing: 1px; }
  .headline-open { top: 172px; font-size: 42px; color: #4a4a4a; transform: scaleX(.78); font-weight: 400; }
  .headline-have { top: 212px; font-size: 72px; color: var(--rose); transform: scaleX(.82); }
  .headline-inside {
    left: 200px; top: 250px; width: 500px; text-align: center;
    font-family: "Yellowtail", cursive; font-size: 178px; line-height: 1.1;
    background: linear-gradient(100deg, var(--gold-dark), var(--gold-light) 45%, var(--gold) 70%, var(--gold-dark));
    -webkit-background-clip: text; background-clip: text; color: transparent;
  }

  .invite { left: 0; width: 889px; text-align: center; }
  .invite-lead { top: 472px; font-size: 24px; color: var(--grey); }
  .invite-title { top: 503px; font-size: 25px; font-weight: 700; color: #dca14a; }

  .date-day { left: 44px; top: 552px; width: 282px; font-size: 31px; letter-spacing: 13px; color: var(--teal); }
  .date-num { left: 40px; top: 580px; width: 290px; font-family: "Bungee Inline", sans-serif; font-size: 96px; line-height: 1; color: var(--gold); letter-spacing: -2px; }
  .date-month { left: 170px; top: 680px; width: 160px; text-align: right; font-size: 31px; letter-spacing: 15px; color: var(--teal); }
  .doors { left: 47px; top: 719px; width: 276px; height: 61px; background: var(--gold); text-align: center; font-size: 21px; line-height: 27px; padding-top: 4px; color: var(--ink); }
  .doors b { color: var(--white); }

  .venue-pin { left: 336px; top: 621px; }
  .venue { left: 374px; top: 605px; width: 490px; height: 114px; border: 2px dashed #8cb7bb; border-radius: 14px; padding: 10px 0 0 60px; }
  .venue-name { font-size: 19px; font-weight: 700; color: var(--teal); line-height: 22px; }
  .venue-note { font-size: 19px; margin-top: 10px; color: var(--ink); }

  .ticket { left: 31px; top: 806px; }
  .guest-note { left: 40px; top: 978px; width: 312px; text-align: center; font-size: 24px; line-height: 30px; color: var(--ink); }

  .speakers-tag { left: 408px; top: 804px; width: 194px; height: 42px; background: var(--teal); border-radius: 14px; color: var(--white); font-weight: 700; font-size: 25px; text-align: center; line-height: 42px; }
  .speakers { left: 408px; top: 860px; width: 460px; font-size: 20px; line-height: 26px; list-style: none; }
  .speakers li { margin-bottom: 9px; }
  .speaker-name { color: #dca14a; font-weight: 700; }

  .contact { left: 0; top: 1049px; width: 889px; height: 77px; background: var(--gold); text-align: center; color: var(--white); }
  .contact-lead { font-size: 20px; padding-top: 8px; }
  .contact-line { font-size: 26px; font-weight: 700; line-height: 32px; }

  .signoff { left: 0; top: 1130px; width: 889px; text-align: center; font-family: "Yellowtail", cursive; font-size: 46px; color: var(--gold); }
</style>
</head>
<body>
<main class="flyer">
  <svg class="abs hero-wash" width="889" height="340" viewBox="0 0 889 340" aria-hidden="true">
    <path d="M0 0H889V320C840 300 800 330 740 312C690 300 640 325 590 296C540 280 500 300 440 290C380 282 340 305 280 296C220 288 160 300 100 290C60 284 30 298 0 292Z" fill="var(--pink)"/>
  </svg>
  <div class="abs mandala-top" role="img" aria-label="Faint line-art mandala ornament"></div>
  <div class="abs mandala-bottom" role="img" aria-label="Faint floral lace ornament"></div>

  <svg class="abs hero-frame" width="889" height="470" viewBox="0 0 889 470" aria-hidden="true">
    <path d="M190 300V29H705V330" fill="none" stroke="var(--white)" stroke-width="5"/>
    <path d="M190 400V453H705V410" fill="none" stroke="var(--gold)" stroke-width="5"/>
  </svg>

  <h1>
    <span class="abs headline headline-411">Get the 411</span>
    <span class="abs headline headline-open">Open yourself up to the info</span>
    <span class="abs headline headline-have">You have</span>
    <span class="abs headline-inside">Inside</span>
  </h1>

  <p class="abs invite invite-lead">Please Join Us For</p>
  <p class="abs invite invite-title">An Evening of Self Discovery, and Enlightment and Fun!</p>

  <p class="abs date-day">THURSDAY</p>
  <p class="abs date-num">11TH</p>
  <p class="abs date-month">APRIL</p>
  <p class="abs doors">Doors Open <b>at 5:30.</b><br>Event from <b>6pm-8pm.</b></p>

  <div class="abs venue">
    <p class="venue-name">The Gardens at Palm Cove- 81200<br>Coral Way Islamorada</p>
    <p class="venue-note">(MM80 Bayside behind Market Hall)</p>
  </div>
  <svg class="abs venue-pin" width="78" height="78" viewBox="0 0 78 78" aria-hidden="true">
    <circle cx="39" cy="39" r="38" fill="var(--pink)"/>
    <path d="M39 20a13 13 0 0 0-13 13c0 10 13 24 13 24s13-14 13-24a13 13 0 0 0-13-13z" fill="var(--white)"/>
    <circle cx="39" cy="33" r="5" fill="var(--pink)"/>
  </svg>

  <svg class="abs ticket" width="332" height="150" viewBox="0 0 332 150" role="img" aria-label="Ticket: $15 each">
    <path d="M8 4H324V58A17 17 0 0 0 324 92V146H8V92A17 17 0 0 0 8 58Z" fill="var(--red)"/>
    <rect x="22" y="18" width="288" height="114" rx="12" fill="none" stroke="var(--white)" stroke-width="2"/>
    <line x1="62" y1="18" x2="62" y2="132" stroke="var(--white)" stroke-width="2"/>
    <line x1="270" y1="18" x2="270" y2="132" stroke="var(--white)" stroke-width="2"/>
    <text x="0" y="0" transform="translate(46 118) rotate(-90)" fill="var(--white)" font-family="Open Sans, sans-serif" font-size="14" letter-spacing="3">TICKET</text>
    <text x="0" y="0" transform="translate(286 32) rotate(90)" fill="var(--white)" font-family="Open Sans, sans-serif" font-size="14" letter-spacing="3">TICKET</text>
    <text x="166" y="95" text-anchor="middle" fill="var(--white)" font-family="Open Sans, sans-serif" font-weight="700" font-size="78" letter-spacing="-3">$15</text>
    <text x="200" y="124" text-anchor="middle" fill="var(--white)" font-family="Open Sans, sans-serif" font-weight="700" font-size="16" letter-spacing="8">EACH</text>
  </svg>
  <p class="abs guest-note">NAMES MUST BE ON<br>THE GUEST LIST</p>

  <h2 class="abs speakers-tag">SPEAKERS:</h2>
  <ul class="abs speakers">
    <li><span class="speaker-name">Marissa Vale-</span> The Bright Path Life Coach- Certified Professional Life Coach</li>
    <li><span class="speaker-name">Celia Brandt-</span> Licensed Hypnotherapist- Lotus Holistic Gifts and Therapies</li>
    <li><span class="speaker-name">Joan Sorrell-</span> Tarot Readings/ Inner Compass Spiritual Counselor</li>
  </ul>

  <div class="abs contact">
    <p class="contact-lead">Contact Marissa Vale for tickets:</p>
    <p class="contact-line">Marissa@brightpathlifecoach.com/ 305-555-0142</p>
  </div>

  <p class="abs signoff">Hope to see you there!</p>
</main>
</body>
</html>
```